BrivoMatex. Lantern for the Steady Growth. Business card

Professional business card for BrivoMatex (Lantern for the Steady Growth)
My rationale: Strategy-> Execution-> Results-> Value that lead to the BrivoMatex name: We put the Lantern for the Steady Growth.
We deliver value to our customers helping them at defining a good strategy (cyan arrow). 90% of well formulated strategies fail due to poor execution so we also consider strategical execution very important (green arrow). Due to the execution we obtain the results (blue arrow). Finally, the results provide feedback to redefine strategy, and the new strategy has to be executed and new results obtained providing new feedback and on and on. It's like a wheel that finally, must create corporate value: value for shareholders, staholders, employees, providers...-

Target Market(s)

CEOs and steering comitees , invewrnent funds

Industry/Entity Type

Business Consultant

Contact Information for Business Card

Tommaso Ferlini
CEO & Founder
tommaso.ferlini@brivomatex.example
Mobile: +34 611.205.938
www.brivomatex.example

Colors

Designer to choose colors to be used in the design.

Requirements
Nice to have
• Nice to hace the words: Strategy, execution, results
• Nice to vave the claim: Lantern for the Steady Growth
• The three colors should be shown:
• cyan for STRATEGY
• green for EXECUTION
• blue for RESULTS
Should not have
• Complete black background

```html
<!DOCTYPE html>
<html lang="en">
<head>
<meta charset="utf-8">
<title>BrivoMatex – Business Card</title>
<link rel="stylesheet" href="https://fonts.googleapis.com/css2?family=Nunito:wght@400;600;800&display=swap">
<style>
  :root {
    --bg: #e8e8e6;
    --paper: #fbfbfa;
    --blue: #2f4a9b;
    --green: #8cc63f;
    --cyan: #2ca7dc;
    --grey: #7d7d7d;
    --ink: #4a4a4a;
  }
  * { box-sizing: border-box; margin: 0; padding: 0; }
  html, body {
    width: 1200px; height: 801px; overflow: hidden;
    background: var(--bg);
    font-family: "Nunito", sans-serif;
  }
  .card {
    position: absolute;
    width: 520px; height: 298px;
    background: var(--paper);
    box-shadow: 0 2px 6px rgba(0,0,0,.12);
    overflow: hidden;
  }
  .card--front { left: 50px; top: 252px; }
  .card--back  { left: 630px; top: 252px; }

  .brand-name {
    color: var(--blue);
    font-weight: 800;
    letter-spacing: -0.5px;
    line-height: 1;
  }
  .card--front .brand-name {
    position: absolute; left: 0; right: 0; top: 36px;
    text-align: center; font-size: 40px;
  }
  .holder {
    position: absolute; left: 0; right: 0; top: 98px; text-align: center;
  }
  .holder__name { color: var(--blue); font-weight: 800; font-size: 17px; letter-spacing: .3px; }
  .holder__role { color: var(--grey); font-size: 12px; margin-top: 2px; letter-spacing: .3px; }

  .contacts {
    position: absolute; left: 38px; right: 30px; top: 160px;
    display: flex; justify-content: center; gap: 22px;
    color: var(--ink); font-size: 11.5px; letter-spacing: .3px;
  }
  .contact { display: flex; align-items: center; gap: 6px; }
  .contact-group { display: flex; flex-direction: column; gap: 4px; }
  .contact--web { padding-left: 22px; }
  .contact__icon { width: 16px; height: 16px; flex: none; }

  .process-band { position: absolute; left: 0; bottom: 0; width: 520px; height: 46px; display: block; }
  .process-band text {
    font-family: "Nunito", sans-serif; font-size: 15px; font-weight: 600;
    fill: #fff; letter-spacing: 1px; text-anchor: middle; dominant-baseline: middle;
  }

  .card--back .logo-lockup {
    position: absolute; left: 0; right: 0; top: 104px; text-align: center;
  }
  .card--back .brand-name { font-size: 58px; }
  .tagline { color: var(--grey); font-size: 16px; margin-top: 8px; letter-spacing: .4px; }
</style>
</head>
<body>

<section class="card card--front" aria-label="Business card front">
  <div class="brand-name">BrivoMatex</div>

  <div class="holder">
    <div class="holder__name">Tommaso Ferlini</div>
    <div class="holder__role">CEO &amp; Founder</div>
  </div>

  <div class="contacts">
    <div class="contact">
      <svg class="contact__icon" viewBox="0 0 16 16" aria-hidden="true">
        <circle cx="8" cy="8" r="8" fill="var(--cyan)"/>
        <path d="M5.2 4.2l1.6-.2.8 2-1 .8c.5 1.1 1.3 1.9 2.4 2.4l.8-1 2 .8-.2 1.6c-3.6.1-6.5-2.8-6.4-6.4z" fill="#fff"/>
      </svg>
      <span>+34 611.205.938</span>
    </div>
    <div class="contact-group">
      <div class="contact">
        <svg class="contact__icon" viewBox="0 0 16 16" aria-hidden="true">
          <circle cx="8" cy="8" r="8" fill="var(--green)"/>
          <rect x="4" y="5.2" width="8" height="5.6" fill="none" stroke="#fff" stroke-width="1"/>
          <path d="M4 5.4l4 3 4-3" fill="none" stroke="#fff" stroke-width="1"/>
        </svg>
        <span>tommaso.ferlini@brivomatex.example</span>
      </div>
      <div class="contact contact--web"><span>www.brivomatex.example</span></div>
    </div>
  </div>

  <svg class="process-band" viewBox="0 0 520 46" aria-label="Strategy, Execution, Results">
    <rect x="0" y="0" width="520" height="46" fill="var(--blue)"/>
    <polygon points="160,0 340,0 340,-0 358,23 340,46 160,46" fill="var(--green)"/>
    <polygon points="0,0 172,0 190,23 172,46 0,46" fill="var(--cyan)"/>
    <text x="90" y="24">STRATEGY</text>
    <text x="268" y="24">EXECUTION</text>
    <text x="440" y="24">RESULTS</text>
  </svg>
</section>

<section class="card card--back" aria-label="Business card back">
  <div class="logo-lockup">
    <div class="brand-name">BrivoMatex</div>
    <div class="tagline">Lantern for the Steady Growth</div>
  </div>
</section>

</body>
</html>
```